Paws Home

Need Yard signs
Dimensions 24" wide and 18" high

Copy: Rescue does not mean "Damaged". It means they have been let down by humans.
Please adopt at: 217 W Brannock Ave, Tampa, Fl 33682
Open: Tues-Sun 10am - 7pm

I have attached a sample of the original ad. I can't use this because the resolution is too low and the type has to be big enough so that it can be seen 12 feet away.
I have also attached some photos you can use. The res may not be hi enough, but perhaps you can find some stock photography even these pics are not hi res enough.

Target Market(s)

animal lovers

Font styles to use
Sans Serif

Colors

Designer to choose colors to be used in the design.

Requirements
Must have
• Must be easy to read.

```html
<!DOCTYPE html>
<html lang="en">
<head>
<meta charset="utf-8">
<title>Paws Home — Yard Sign</title>
<link href="https://fonts.googleapis.com/css2?family=Fira+Sans+Condensed:wght@600;700&display=swap" rel="stylesheet">
<style>
  :root {
    --backdrop: #e9e7e3;
    --sign-dark: #211e1e;
    --photo-warm: #c97a3a;
    --photo-amber: #e3a66b;
    --photo-shadow: #3a2a22;
    --headline: #ffffff;
    --info: #f2c98f;
    --web: #ffffff;
  }
  * { margin: 0; padding: 0; box-sizing: border-box; }
  html, body {
    width: 1200px;
    height: 675px;
    overflow: hidden;
    background: var(--backdrop);
  }
  .canvas {
    width: 1200px;
    height: 675px;
    display: flex;
    align-items: center;
    justify-content: center;
  }
  .yard-sign {
    position: relative;
    width: 840px;
    height: 630px;
    background: var(--sign-dark);
    overflow: hidden;
    box-shadow: 0 6px 24px rgba(0,0,0,0.18);
    font-family: "Fira Sans Condensed", "Arial Narrow", sans-serif;
  }
  .dog-photo {
    position: absolute;
    left: 0;
    top: 0;
    width: 620px;
    height: 630px;
    background:
      linear-gradient(90deg, rgba(33,30,30,0) 0%, rgba(33,30,30,0) 62%, var(--sign-dark) 100%),
      radial-gradient(ellipse at 40% 35%, var(--photo-amber) 0%, var(--photo-warm) 45%, var(--photo-shadow) 100%);
  }
  .message {
    position: absolute;
    right: 34px;
    top: 44px;
    text-align: right;
    color: var(--headline);
    font-weight: 700;
    font-size: 46px;
    line-height: 1.12;
    text-transform: uppercase;
    letter-spacing: 0.3px;
  }
  .adopt-info {
    position: absolute;
    right: 34px;
    top: 360px;
    text-align: right;
    color: var(--info);
    font-weight: 600;
    font-size: 27px;
    line-height: 1.3;
  }
  .adopt-info .lead { text-transform: uppercase; }
  .website {
    position: absolute;
    right: 34px;
    bottom: 36px;
    color: var(--web);
    font-weight: 600;
    font-size: 19px;
  }
</style>
</head>
<body>
  <main class="canvas">
    <section class="yard-sign">
      <div class="dog-photo" role="img" aria-label="Photograph of a sad black Labrador looking out through the bars of a shelter kennel, warm orange background"></div>
      <h1 class="message">
        'Rescue' does not<br>
        mean 'damaged'<br>
        it means they have<br>
        been let down<br>
        by humans
      </h1>
      <p class="adopt-info">
        <span class="lead">Please adopt at:</span><br>
        217 W Brannock Ave,<br>
        Tampa, Fl 33682<br>
        Open: Tues-Sun<br>
        10am - 7pm
      </p>
      <p class="website">pawshomerescue.org</p>
    </section>
  </main>
</body>
</html>
```